Flyer for spiritual retreat (yoga, meditation, reiki, raw food)

I would like a flyer to promote my upcoming retreat and a matching Facebook banner.

The name of the retreat is "Wavecrest Of Calm" and the tagline is "retreat into you"

The activities in the retreat include daily meditation, ecstatic dance, spiritual development workshops on intuition, energy healing etc and a reiki session is included.

I would like a flyer designed to promote this, something that is editable as I will be running this multiple times and will need to adjust the flyer to add the dates etc each time.

edit: add that here will be fully catered raw food and juices, and that the retreat price includes all accomodation, meals and workshops.

Please contact me if you need further info. Please also visit my website www.marithovland.com and www.facebook.com/tolvanahaven to see my current events and promotions.

Thank you,

Marit

Reason: Hi all, thank you all for your submissions. Apologies as I am traveling and do not have much access to internet and will review your submissions and provide feedback as soon as possible. Kind regards, Marit.

Target Market(s)

People who like meditation, yoga, fans of rowan mabry and jasper vinek, those interested in personal and spiritual development.

Industry/Entity Type

Health And Wellness

Requirements
Must have
• Please put the included reiki session as as added bonus. Something like "BONUS 30 minute reiki healing session" in a little star/banner/something that stands out.
• Please emphasise the "light" part of Wavecrest as I am going for a play on words between in the light and enlightenment.
• Please include placeholder text for place, location, time
• Placeholder for price
• My name (see attached file - can change colour to suit) and website (www.marithovland.com)
Nice to have
• I prefer rounded designs, curves rather than block designs.
Should not have
• Tolvana Haven logo

```html
<!DOCTYPE html>
<html lang="en">
<head>
<meta charset="utf-8">
<title>Wavecrest Of Calm – Retreat Flyer</title>
<link href="https://fonts.googleapis.com/css2?family=Great+Vibes&family=Montserrat:wght@300;400;700;800&family=Merriweather+Sans:wght@300;400;700;800&display=swap" rel="stylesheet">
<style>
  :root{
    --stage:#b9b9bb;
    --paper:#ffffff;
    --ink:#3a3a55;
    --navy:#2f2d6e;
    --purple:#4a3f8f;
    --purple-soft:#5b5196;
    --sky:#1f9fe0;
    --sky-light:#8fd0ee;
    --sky-pale:#cfeaf7;
    --slate:#5c5b78;
    --white:#ffffff;
  }
  *{margin:0;padding:0;box-sizing:border-box}
  html,body{width:1200px;height:1011px;overflow:hidden;background:var(--stage)}
  .flyer{
    position:absolute;left:260px;top:24px;width:680px;height:962px;
    background:var(--paper);overflow:hidden;
    font-family:"Merriweather Sans",sans-serif;color:var(--ink);
  }
  .portrait{
    position:absolute;left:0;top:104px;width:362px;height:480px;
    background:linear-gradient(135deg,#7fb35a 0%,#a9c98a 30%,#d9cfc4 55%,#c66b3e 80%,#6f4a3a 100%);
  }
  .portrait-stripe{position:absolute;left:362px;top:104px;width:16px;height:470px;background:var(--sky)}
  .wave{position:absolute;left:0;top:0;width:680px;height:962px}
  .signature{
    position:absolute;left:250px;top:34px;
    font-family:"Great Vibes",cursive;font-size:62px;color:#2b2b2b;
  }
  .title{position:absolute;left:392px;top:150px;width:280px}
  .title-rule{height:2px;background:var(--navy);margin-left:40px;width:220px}
  .title-wave{font-family:"Montserrat",sans-serif;font-weight:300;font-size:42px;color:var(--navy);margin-top:14px;line-height:1}
  .title-crest{font-family:"Montserrat",sans-serif;font-size:62px;color:var(--sky);line-height:1.05;letter-spacing:1px}
  .title-crest b{font-weight:800}
  .title-crest span{font-weight:300}
  .title-calm{font-family:"Montserrat",sans-serif;font-weight:400;font-size:36px;color:var(--navy);text-align:right;padding-right:20px;line-height:1.1}
  .title-rule.lower{margin:10px 0 0 0;width:240px}
  .tagline{
    position:absolute;left:384px;top:356px;width:290px;display:flex;align-items:center;gap:10px;
    font-family:"Montserrat",sans-serif;font-size:17px;letter-spacing:1.5px;color:var(--ink);white-space:nowrap;
  }
  .tagline::before,.tagline::after{content:"";flex:1;height:1px;background:#999}
  .bonus{position:absolute;left:452px;top:370px;width:210px;height:210px}
  .bonus-text{
    position:absolute;left:452px;top:420px;width:210px;text-align:center;color:var(--white);
    font-family:"Montserrat",sans-serif;line-height:1.05;
  }
  .bonus-text .big{font-weight:800;font-size:26px;display:block}
  .bonus-text .mid{font-size:17px;display:block}
  .bonus-text .hl{font-size:16px;font-weight:700;color:var(--sky-light);display:block}
  .bonus-text .end{font-size:24px;display:block}
  .activities-label{
    position:absolute;left:40px;top:604px;padding:8px 22px;border-radius:14px;
    background:var(--purple-soft);color:var(--white);font-weight:800;font-size:26px;
  }
  .activities{position:absolute;left:50px;top:658px;list-style:none;font-size:19px;color:var(--ink);line-height:27px}
  .activities li{display:flex;align-items:center;gap:14px}
  .activities svg{width:14px;height:14px;flex:none}
  .ribbon{position:absolute;left:0;top:0;width:680px;height:962px}
  .event{position:absolute;left:60px;top:780px;width:560px;color:var(--white)}
  .event-row{display:flex;justify-content:space-around;align-items:center;font-weight:800;font-size:19px}
  .event-row span{display:flex;align-items:center;gap:8px}
  .event-row svg{width:20px;height:20px}
  .event-note{text-align:center;font-size:11px;margin-top:8px;opacity:.9}
  .cost{position:absolute;left:140px;top:856px;text-align:center}
  .cost-line{font-weight:700;font-size:38px;color:var(--slate);line-height:1}
  .cost-line em{font-style:normal;color:var(--sky);font-weight:800}
  .cost-note{font-size:11px;color:var(--ink)}
  .divider{position:absolute;left:388px;top:862px;width:1px;height:40px;background:#8a8aa0}
  .site{position:absolute;left:404px;top:872px;display:flex;align-items:center;gap:8px;font-size:17px;color:var(--slate);white-space:nowrap}
  .site b{font-weight:800}
  .footer{
    position:absolute;left:0;bottom:0;width:680px;height:48px;background:var(--slate);
    display:flex;align-items:center;padding-left:40px;gap:10px;color:var(--white);font-size:15px;font-weight:700;
  }
  .footer i{display:block;width:16px;height:16px;border-radius:50%;background:var(--white)}
</style>
</head>
<body>
<div class="flyer">
  <div class="portrait" role="img" aria-label="Portrait photograph of Marit smiling in a colourful patterned top in front of tropical greenery"></div>
  <div class="portrait-stripe"></div>

  <svg class="wave" viewBox="0 0 680 962" aria-hidden="true">
    <defs>
      <linearGradient id="sea" x1="0" y1="0" x2="0" y2="1">
        <stop offset="0" stop-color="#7cc6e8"/>
        <stop offset="1" stop-color="#bfe2f3"/>
      </linearGradient>
      <linearGradient id="band" x1="0" y1="0" x2="1" y2="0">
        <stop offset="0" stop-color="#4b3f92"/>
        <stop offset=".5" stop-color="#6f79c4"/>
        <stop offset="1" stop-color="#3d3a8c"/>
      </linearGradient>
    </defs>
    <path d="M0 610 C140 520 300 500 430 505 C540 508 620 470 680 430 L680 962 L0 962 Z" fill="#d4ecf8" opacity=".8"/>
    <path d="M0 628 C150 545 300 525 430 528 C545 530 625 490 680 455 L680 962 L0 962 Z" fill="url(#sea)"/>
  </svg>

  <div class="signature">Marit Hovland</div>

  <div class="title">
    <div class="title-rule"></div>
    <div class="title-wave">Wave</div>
    <div class="title-crest"><b>CRE</b><span>ST</span></div>
    <div class="title-calm">Of Calm</div>
    <div class="title-rule lower"></div>
  </div>
  <div class="tagline">RETREAT INTO YOU</div>

  <svg class="bonus" viewBox="-105 -105 210 210" aria-hidden="true">
    <polygon fill="#3d3a8c" stroke="#5db8e6" stroke-width="4"
      points="0,-98 20,-64 56,-80 50,-42 92,-34 62,-6 94,22 54,32 66,70 28,58 8,96 -12,60 -50,80 -46,40 -90,30 -60,4 -96,-28 -54,-36 -62,-76 -24,-60"/>
  </svg>
  <div class="bonus-text">
    <span class="big">BONUS</span>
    <span class="mid">30 minute</span>
    <span class="hl">reiki healing</span>
    <span class="end">session</span>
  </div>

  <div class="activities-label">The activities</div>
  <ul class="activities">
    <li><svg viewBox="0 0 14 14"><path d="M2 6 L6 11 L12 2" fill="none" stroke="#5b5196" stroke-width="2.5"/></svg>daily meditation,</li>
    <li><svg viewBox="0 0 14 14"><path d="M2 6 L6 11 L12 2" fill="none" stroke="#5b5196" stroke-width="2.5"/></svg>ecstatic dance,</li>
    <li><svg viewBox="0 0 14 14"><path d="M2 6 L6 11 L12 2" fill="none" stroke="#5b5196" stroke-width="2.5"/></svg>spiritual development workshops on intuition,</li>
    <li><svg viewBox="0 0 14 14"><path d="M2 6 L6 11 L12 2" fill="none" stroke="#5b5196" stroke-width="2.5"/></svg>energy healing etc</li>
  </ul>

  <svg class="ribbon" viewBox="0 0 680 962" aria-hidden="true">
    <polygon points="10,838 52,838 52,862 10,862 24,850" fill="#4b4a6e"/>
    <polygon points="628,760 672,760 658,772 672,784 628,784" fill="#4b4a6e"/>
    <rect x="40" y="768" width="600" height="82" fill="url(#band)"/>
  </svg>
  <div class="event">
    <div class="event-row">
      <span><svg viewBox="0 0 20 20"><rect x="2" y="4" width="16" height="14" rx="2" fill="none" stroke="#fff" stroke-width="2"/><line x1="2" y1="8" x2="18" y2="8" stroke="#fff" stroke-width="2"/></svg>1st January, 2017</span>
      <span><svg viewBox="0 0 20 20"><path d="M10 19 C4 12 4 9 4 8 a6 6 0 0 1 12 0 c0 1 0 4 -6 11z" fill="#fff"/><circle cx="10" cy="8" r="2.3" fill="#5b5196"/></svg></span>
      <span><svg viewBox="0 0 20 20"><circle cx="10" cy="10" r="8" fill="none" stroke="#fff" stroke-width="2"/><path d="M10 5 V10 H14" fill="none" stroke="#fff" stroke-width="2"/></svg>4 pm onward</span>
    </div>
    <div class="event-note">Fully catered with raw food and fresh juices throughout the retreat</div>
  </div>

  <div class="cost">
    <div class="cost-line">Cost <em>$150</em></div>
    <div class="cost-note">(includes all accomodation, meals and workshops.)</div>
  </div>
  <div class="divider"></div>
  <div class="site">
    <svg width="18" height="18" viewBox="0 0 20 20" aria-hidden="true"><circle cx="10" cy="10" r="8" fill="none" stroke="#5c5b78" stroke-width="1.8"/><ellipse cx="10" cy="10" rx="3.5" ry="8" fill="none" stroke="#5c5b78" stroke-width="1.5"/><line x1="2" y1="10" x2="18" y2="10" stroke="#5c5b78" stroke-width="1.5"/></svg>
    <span>www.<b>marithovland</b>.com</span>
  </div>

  <div class="footer"><i></i>www.facebook.com/tolvanahaven</div>
</div>
</body>
</html>
```